Brochure for Varosh Law firm

We would like to have a brochure that describes the Firm ( about the firm) , the vision, the team , the practice areas. And the contact.
Varosh law firm has ranked as top Libyan law firms by Juris Panel.
It will give a good picture if you look at www.varosh-example.ly

We can also provide more information if requested to share with designer.

```html
<!DOCTYPE html>
<html lang="en">
<head>
<meta charset="utf-8">
<title>Varosh Law firm brochure</title>
<link rel="stylesheet" href="https://fonts.googleapis.com/css2?family=Montserrat:wght@300;400;600;700;800&family=Open+Sans:wght@400;600&display=swap">
<style>
:root{
  --blue:#0b47b3;
  --blue-deep:#083a9c;
  --ink:#1c1c2b;
  --grey:#eeeff1;
  --grey-line:#cfd1d6;
  --white:#ffffff;
  --page:#e6e6e8;
  --photo-warm:#b8a89a;
  --photo-cool:#8d96a6;
}
*{margin:0;padding:0;box-sizing:border-box}
html,body{width:828px;height:1200px;overflow:hidden;background:var(--page)}
body{position:relative;font-family:"Open Sans",Arial,sans-serif;color:var(--ink)}
.spread{position:absolute;left:54px;width:720px;height:540px;overflow:hidden;background:var(--grey);box-shadow:0 6px 18px rgba(0,0,0,.15)}
.spread--outside{top:40px}
.spread--inside{top:620px}
.spread svg.shapes{position:absolute;left:0;top:0}
.abs{position:absolute}
.h-thin{font-family:"Montserrat",sans-serif;font-weight:300}
.h-bold{font-family:"Montserrat",sans-serif;font-weight:800}
.white{color:var(--white)}
.blue{color:var(--blue)}

/* outside */
.about{left:18px;top:40px;width:205px;font-size:8.6px;line-height:1.45;color:var(--white)}
.clients-title{left:30px;top:372px;font-size:19px;color:var(--blue)}
.client-grid{left:30px;top:402px;width:190px;display:grid;grid-template-columns:repeat(3,1fr);gap:4px}
.client{height:34px;background:var(--grey);border:1px solid var(--grey-line);display:flex;align-items:center;justify-content:center;font-family:"Open Sans",sans-serif;font-weight:600;font-size:8.5px;color:#55575e}
.testi-head{left:262px;top:28px}
.testi-head .h-thin{font-size:17px;display:block;line-height:1.1}
.testi-head .h-bold{font-size:17px;color:var(--blue);line-height:1.1}
.rule{height:1px;background:var(--blue)}
.quote{left:262px;width:205px;font-size:7.4px;line-height:1.35;padding-left:16px}
.quote::before{content:"\201C";position:absolute;left:0;top:-6px;font:800 24px "Montserrat",sans-serif;color:#777}
.quote .src{display:block;text-align:right;font:700 7.6px "Montserrat",sans-serif;color:var(--blue);margin-top:2px}
.contact-title{left:262px;top:410px;font-size:17px;color:var(--white)}
.office{font-size:7.4px;line-height:1.45;color:var(--white)}
.office b{display:block;font:700 7.8px "Montserrat",sans-serif;margin-bottom:2px}
.web{font:600 8.6px "Montserrat",sans-serif;color:var(--white);display:flex;align-items:center;gap:5px}
.brand{left:512px;top:26px;font:700 30px "Montserrat",sans-serif;color:var(--ink);letter-spacing:-.5px}
.cover-title{left:505px;top:340px;font-size:21px;line-height:1.2;color:var(--white)}
.cover-tag{left:505px;top:420px;font-size:9px;line-height:1.4;color:var(--white)}

/* inside */
.svc-head{left:24px;top:34px;font-size:17px;color:var(--white)}
.svc-list{width:210px}
.svc{display:flex;align-items:center;gap:10px;margin-bottom:20px}
.svc .dot{flex:none;width:36px;height:36px;border-radius:50%;background:var(--white);display:flex;align-items:center;justify-content:center;box-shadow:0 2px 5px rgba(0,0,0,.25)}
.svc h3{font:700 9.6px "Montserrat",sans-serif;color:var(--white)}
.svc p{font-size:7.4px;line-height:1.35;color:#dfe6f7}
.ip-head{left:500px;top:30px}
.ip-head .h-thin{font-size:16px;display:block}
.ip-head .h-bold{font-size:16px;color:var(--blue);line-height:1.15}
.ip-text{left:500px;top:112px;width:200px;font-size:7.6px;line-height:1.45}
.ip-list{left:500px;top:228px;width:205px}
.ip{display:flex;align-items:center;gap:10px;margin-bottom:16px}
.ip .dot{flex:none;width:34px;height:34px;border-radius:50%;background:var(--blue);border:3px solid var(--white);box-shadow:0 2px 5px rgba(0,0,0,.25);display:flex;align-items:center;justify-content:center;font:800 11px "Montserrat",sans-serif;color:var(--white)}
.ip h3{font:700 9.4px "Montserrat",sans-serif;color:var(--blue)}
.ip p{font-size:7.2px;line-height:1.35}
.ask{left:500px;top:494px;font:800 10px "Montserrat",sans-serif;color:var(--blue)}
</style>
</head>
<body>

<!-- Outside spread -->
<section class="spread spread--outside">
  <svg class="shapes" width="720" height="540" viewBox="0 0 720 540">
    <defs>
      <linearGradient id="stoneGrad" x1="0" y1="0" x2="1" y2="1">
        <stop offset="0" stop-color="#9a9a9a"/><stop offset="1" stop-color="#4d4d4d"/>
      </linearGradient>
      <linearGradient id="officeGrad" x1="0" y1="0" x2="1" y2="1">
        <stop offset="0" stop-color="#4a4f5c"/><stop offset="1" stop-color="#c9ccd3"/>
      </linearGradient>
    </defs>
    <rect x="0" y="0" width="240" height="540" fill="#ffffff"/>
    <path d="M0 0H240V235Q190 300 0 335Z" fill="var(--blue)"/>
    <rect x="38" y="150" width="178" height="186" fill="#ffffff" transform="rotate(-4 127 243)"/>
    <rect x="46" y="158" width="162" height="170" fill="url(#stoneGrad)" transform="rotate(-4 127 243)" role="img" aria-label="Black and white photo of an ancient stone archway"/>
    <path d="M240 410Q370 400 480 315V540H240Z" fill="var(--blue)"/>
    <path d="M255 405l22 -12l-6 20z" fill="#2a2a3a"/>
    <path d="M520 82H720V250Q630 300 540 262Q520 200 520 82Z" fill="url(#officeGrad)" role="img" aria-label="Photo of lawyers in suits working at a desk with a laptop and gavel"/>
    <path d="M505 120l32 -10l-14 30z" fill="var(--blue)"/>
    <path d="M480 305Q600 320 720 250V540H480Z" fill="var(--blue)"/>
    <path d="M665 255l16 -18l4 22z" fill="#ffffff"/>
    <line x1="240" y1="0" x2="240" y2="540" stroke="rgba(0,0,0,.08)"/>
    <line x1="480" y1="0" x2="480" y2="540" stroke="rgba(0,0,0,.08)"/>
  </svg>

  <p class="abs about">Varosh Law is a law firm established in Tripoli, Libya, in 2005. The Firm brings together some of the most experienced legal practitioners and scholars in Libya. In addition to our head offices in Tripoli, our first regional office was launched in Benghazi.</p>

  <h2 class="abs h-bold clients-title">Clients</h2>
  <div class="abs client-grid">
    <div class="client">Corvalis</div><div class="client">Brenmark</div><div class="client">Lumora</div>
    <div class="client">Petrovane</div><div class="client">Netharbor</div><div class="client">Kestrel</div>
    <div class="client">Searlo</div><div class="client">Halvern</div><div class="client">Meridane</div>
  </div>

  <div class="abs testi-head">
    <span class="h-thin">Clients'</span>
    <span class="h-bold">Testimonials</span>
    <div class="rule" style="width:190px;margin-top:4px"></div>
  </div>
  <p class="abs quote" style="top:78px">Varosh Law operates in a genuine niche as a law firm providing international law firm levels of support and responsiveness in connection with the Libyan jurisdiction.<span class="src">Juris Panel</span></p>
  <p class="abs quote" style="top:146px">Salem Haddar has unrivalled expertise in the Libyan legal market. He also has excellent local knowledge which informs his legal advice. We consider Varosh to be the premier law firm in this market.<span class="src">Juris Panel</span></p>
  <p class="abs quote" style="top:214px">In-depth knowledge of Libyan laws and regulations... practical know-how of how the Libyan public sector actually functions in Libya, the procedural, registration and documentary requirements associated with a transaction are often opaque and it is essential to seek guidance from an adviser who can offer more than a purely written analysis of the laws themselves.<span class="src">Juris Panel</span></p>

  <h2 class="abs contact-title"><span class="h-thin">Contact</span> <span class="h-bold">us</span></h2>
  <div class="abs rule" style="left:262px;top:434px;width:200px;background:#fff"></div>
  <div class="abs office" style="left:262px;top:444px;width:100px">
    <b>Tripoli Office</b>
    12, Harbor Tower 2<br>P.O. Box 40210<br>Tripoli, Libya<br>+218 21 000 0101
  </div>
  <div class="abs office" style="left:370px;top:444px;width:105px">
    <b>Benghazi Office</b>
    Sample Street, Garden District<br>Benghazi, Libya<br>+218 92 000 0202
  </div>
  <div class="abs web" style="left:262px;top:512px">
    <svg width="10" height="10" viewBox="0 0 10 10" aria-hidden="true"><circle cx="5" cy="5" r="4.2" fill="none" stroke="#fff"/><line x1="1" y1="5" x2="9" y2="5" stroke="#fff" stroke-width=".8"/><ellipse cx="5" cy="5" rx="1.8" ry="4.2" fill="none" stroke="#fff" stroke-width=".8"/></svg>
    www.varosh-example.ly
  </div>

  <div class="abs brand">Varosh</div>
  <h1 class="abs h-bold cover-title">Setting<br>The Standard<br>For Libya</h1>
  <p class="abs cover-tag">Excellence is the<br>hallmark of our legal solutions.</p>
  <div class="abs rule" style="left:505px;top:452px;width:190px;background:#fff"></div>
  <div class="abs web" style="left:505px;top:464px">
    <svg width="10" height="10" viewBox="0 0 10 10" aria-hidden="true"><circle cx="5" cy="5" r="4.2" fill="none" stroke="#fff"/><line x1="1" y1="5" x2="9" y2="5" stroke="#fff" stroke-width=".8"/><ellipse cx="5" cy="5" rx="1.8" ry="4.2" fill="none" stroke="#fff" stroke-width=".8"/></svg>
    www.varosh-example.ly
  </div>
</section>

<!-- Inside spread -->
<section class="spread spread--inside">
  <svg class="shapes" width="720" height="540" viewBox="0 0 720 540">
    <defs>
      <linearGradient id="meetGrad" x1="0" y1="0" x2="1" y2="1">
        <stop offset="0" stop-color="#d9d6d2"/><stop offset=".5" stop-color="var(--photo-warm)"/><stop offset="1" stop-color="#e8e2da"/>
      </linearGradient>
      <linearGradient id="meetGrad2" x1="0" y1="0" x2="1" y2="1">
        <stop offset="0" stop-color="#c7ccd6"/><stop offset="1" stop-color="#a89a8a"/>
      </linearGradient>
    </defs>
    <rect x="0" y="0" width="480" height="540" fill="var(--blue)"/>
    <rect x="480" y="0" width="240" height="540" fill="var(--grey)"/>
    <path d="M0 420Q130 370 250 392V540H0Z" fill="url(#meetGrad)" role="img" aria-label="Photo of two colleagues reviewing documents at a meeting table"/>
    <path d="M250 392Q380 410 480 335L520 540H250Z" fill="url(#meetGrad2)" role="img" aria-label="Photo of a woman and an older man signing papers at a desk"/>
    <line x1="240" y1="0" x2="240" y2="540" stroke="rgba(0,0,0,.1)"/>
    <line x1="480" y1="0" x2="480" y2="540" stroke="rgba(0,0,0,.1)"/>
  </svg>

  <h2 class="abs svc-head"><span class="h-thin">Varosh Law</span> <span class="h-bold">Services</span></h2>
  <div class="abs rule" style="left:24px;top:60px;width:200px;background:#fff"></div>
  <div class="abs svc-list" style="left:24px;top:78px">
    <div class="svc"><span class="dot"><svg width="18" height="18" viewBox="0 0 18 18" aria-hidden="true"><circle cx="5" cy="5" r="2.2" fill="none" stroke="#0b47b3" stroke-width="1.3"/><circle cx="13" cy="5" r="2.2" fill="none" stroke="#0b47b3" stroke-width="1.3"/><path d="M1 15q4-7 8 0M9 15q4-7 8 0" fill="none" stroke="#0b47b3" stroke-width="1.3"/></svg></span><div><h3>Consultation</h3><p>Varosh provides consultation legal practice in Libya</p></div></div>
    <div class="svc"><span class="dot"><svg width="18" height="18" viewBox="0 0 18 18" aria-hidden="true"><rect x="3" y="3" width="8" height="4" rx="1" transform="rotate(-35 7 5)" fill="none" stroke="#0b47b3" stroke-width="1.3"/><line x1="8" y1="8" x2="14" y2="15" stroke="#0b47b3" stroke-width="1.5"/><line x1="2" y1="16" x2="10" y2="16" stroke="#0b47b3" stroke-width="1.3"/></svg></span><div><h3>Litigation</h3><p>Varosh provides Litigation practice in Libya</p></div></div>
    <div class="svc"><span class="dot"><svg width="18" height="18" viewBox="0 0 18 18" aria-hidden="true"><line x1="9" y1="2" x2="9" y2="15" stroke="#0b47b3" stroke-width="1.3"/><line x1="3" y1="4" x2="15" y2="4" stroke="#0b47b3" stroke-width="1.3"/><path d="M1 10l2-6 2 6zM13 10l2-6 2 6z" fill="none" stroke="#0b47b3" stroke-width="1.1"/><line x1="5" y1="16" x2="13" y2="16" stroke="#0b47b3" stroke-width="1.3"/></svg></span><div><h3>Arbitration</h3><p>Varosh provides arbitration legal practice in Libya</p></div></div>
    <div class="svc"><span class="dot"><svg width="18" height="18" viewBox="0 0 18 18" aria-hidden="true"><rect x="4" y="2" width="10" height="14" fill="none" stroke="#0b47b3" stroke-width="1.3"/><line x1="6" y1="6" x2="12" y2="6" stroke="#0b47b3"/><line x1="6" y1="9" x2="12" y2="9" stroke="#0b47b3"/><line x1="6" y1="12" x2="10" y2="12" stroke="#0b47b3"/></svg></span><div><h3>Commercial Registration</h3><p>Varosh provides commercial registration services in Libya</p></div></div>
  </div>

  <div class="abs svc-list" style="left:262px;top:52px">
    <div class="svc"><span class="dot"><svg width="18" height="18" viewBox="0 0 18 18" aria-hidden="true"><rect x="3" y="2" width="12" height="14" fill="none" stroke="#0b47b3" stroke-width="1.3"/><line x1="5" y1="6" x2="13" y2="6" stroke="#0b47b3"/><circle cx="11" cy="12" r="2" fill="none" stroke="#0b47b3"/></svg></span><div><h3>Investment Licence</h3><p>Varosh provides investment licence services in Libya</p></div></div>
    <div class="svc"><span class="dot"><svg width="18" height="18" viewBox="0 0 18 18" aria-hidden="true"><rect x="3" y="3" width="10" height="13" fill="none" stroke="#0b47b3" stroke-width="1.3"/><path d="M5 8l1.5 1.5 3-3" fill="none" stroke="#0b47b3"/><path d="M11 16l4-7 2 4z" fill="none" stroke="#0b47b3"/></svg></span><div><h3>Legal Risk Assessment</h3><p>Varosh provides legal risk assessment services in Libya</p></div></div>
    <div class="svc"><span class="dot"><svg width="18" height="18" viewBox="0 0 18 18" aria-hidden="true"><rect x="4" y="2" width="11" height="14" rx="1" fill="none" stroke="#0b47b3" stroke-width="1.3"/><circle cx="9.5" cy="7" r="2" fill="none" stroke="#0b47b3"/><path d="M6 13q3.5-4 7 0" fill="none" stroke="#0b47b3"/></svg></span><div><h3>Due-Diligence</h3><p>Varosh provides due-diligence services in Libya</p></div></div>
    <div class="svc"><span class="dot"><svg width="18" height="18" viewBox="0 0 18 18" aria-hidden="true"><path d="M9 2l5 2v4q0 4-5 6-5-2-5-6V4z" fill="none" stroke="#0b47b3" stroke-width="1.3"/><path d="M6.5 8l2 2 3-3.5" fill="none" stroke="#0b47b3"/></svg></span><div><h3>Intellectual Property</h3><p>Varosh provides intellectual property services in Libya</p></div></div>
  </div>

  <div class="abs ip-head">
    <span class="h-thin">Intellectual</span>
    <span class="h-bold">Property Services<br>in Libya</span>
    <div class="rule" style="width:195px;margin-top:5px"></div>
  </div>
  <p class="abs ip-text">We offer our clients a full range of IP services, including processing applications for trademark, patent, copyright and design protection, conducting prior art searches, acting in IP litigation, drafting and negotiating IP contracts, and providing consultation spanning across Libyan aspects of intellectual property laws and regulations.</p>
  <div class="abs ip-list">
    <div class="ip"><span class="dot">TM</span><div><h3>Trademark</h3><p>Varosh Firm provides trademark services in Libya</p></div></div>
    <div class="ip"><span class="dot">P</span><div><h3>Patent</h3><p>Varosh Firm provides patent registration services in Libya</p></div></div>
    <div class="ip"><span class="dot">C</span><div><h3>Copyright</h3><p>Varosh Firm provides copyright services in Libya</p></div></div>
    <div class="ip"><span class="dot"><svg width="14" height="14" viewBox="0 0 14 14" aria-hidden="true"><rect x="2" y="2" width="10" height="10" fill="none" stroke="#fff" stroke-width="1.4"/><line x1="7" y1="2" x2="7" y2="12" stroke="#fff"/><line x1="2" y1="7" x2="12" y2="7" stroke="#fff"/></svg></span><div><h3>Addons Services</h3><p>Varosh provides addons services in Libya</p></div></div>
  </div>
  <p class="abs ask">Ask Varosh Online for Non Corporate</p>
</section>

</body>
</html>
```